Stationery and Business Card Design

We need stationary design for our new company pelvanta. Pelvanta is a company that provides city apartment rentals for tourists in Athens We need business cards, letterheads for A4 and A5 and envelopes for A4 A5. The design needs to be modern, friendly and corporate.

Target Market(s)

City Tourists

Industry/Entity Type

Tourism

```html
<!DOCTYPE html>
<html lang="en">
<head>
<meta charset="utf-8">
<title>Pelvanta Business Card</title>
<link rel="stylesheet" href="https://fonts.googleapis.com/css2?family=Hind:wght@400;600&display=swap">
<style>
  :root {
    --brand-magenta: #961f5a;
    --brand-charcoal: #363234;
    --text-grey: #444446;
    --mark-black: #222222;
    --paper: #ffffff;
  }
  html, body {
    margin: 0;
    padding: 0;
    width: 1200px;
    height: 1200px;
    overflow: hidden;
    background: var(--paper);
    font-family: "Hind", sans-serif;
  }
  .sheet {
    position: relative;
    width: 1200px;
    height: 1200px;
  }
  .crop-marks {
    position: absolute;
    left: 0;
    top: 0;
  }
  .brand-lockup {
    position: absolute;
    display: flex;
    flex-direction: column;
    align-items: center;
  }
  .brand-square {
    width: 44px;
    height: 44px;
    background: var(--brand-magenta);
  }
  .brand-name {
    margin-top: 6px;
    font-size: 31px;
    font-weight: 400;
    line-height: 1;
    color: var(--brand-magenta);
    letter-spacing: -0.3px;
  }
  .front-lockup { left: 137px; top: 559px; width: 147px; }
  .back-lockup { left: 793px; top: 519px; width: 148px; }

  .contact-block {
    position: absolute;
    left: 306px;
    top: 512px;
    font-size: 12.5px;
    line-height: 14px;
    color: var(--text-grey);
    white-space: nowrap;
  }
  .contact-block p { margin: 0; }
  .contact-block .group + .group { margin-top: 14px; }
  .contact-name {
    font-weight: 600;
    font-size: 13.5px;
    color: var(--brand-magenta);
  }
  .back-band-dark {
    position: absolute;
    left: 644px;
    top: 645px;
    width: 444px;
    height: 24px;
    background: var(--brand-charcoal);
  }
  .back-band-magenta {
    position: absolute;
    left: 644px;
    top: 669px;
    width: 444px;
    height: 54px;
    background: var(--brand-magenta);
  }
</style>
</head>
<body>
<main class="sheet">
  <!-- Card front -->
  <div class="brand-lockup front-lockup">
    <div class="brand-square"></div>
    <div class="brand-name">Pelvanta</div>
  </div>

  <div class="contact-block">
    <div class="group">
      <p class="contact-name">Eleni Marou</p>
      <p>General Manager</p>
      <p>M. +30 690 555 7788</p>
      <p>eleni.marou@pelvantastays.com</p>
    </div>
    <div class="group">
      <p>Odos Ermou 48, Monastiraki,</p>
      <p>Plaka, Athens 105 63</p>
      <p>Attica - Central Greece, Greece</p>
    </div>
    <div class="group">
      <p>T. +30 210 555 0142/43</p>
      <p>F. +30 210 5550144</p>
      <p>www.pelvanta.com</p>
    </div>
  </div>

  <!-- Card back -->
  <div class="brand-lockup back-lockup">
    <div class="brand-square"></div>
    <div class="brand-name">Pelvanta</div>
  </div>
  <div class="back-band-dark"></div>
  <div class="back-band-magenta"></div>

  <!-- Trim marks -->
  <svg class="crop-marks" width="1200" height="1200" viewBox="0 0 1200 1200" aria-hidden="true">
    <g stroke="var(--mark-black)" stroke-width="1.6" fill="none">
      <line x1="116" y1="424" x2="116" y2="457"/>
      <line x1="514" y1="424" x2="514" y2="457"/>
      <line x1="116" y1="724" x2="116" y2="756"/>
      <line x1="514" y1="724" x2="514" y2="756"/>
      <line x1="60" y1="479" x2="93" y2="479"/>
      <line x1="537" y1="479" x2="570" y2="479"/>
      <line x1="60" y1="701" x2="93" y2="701"/>
      <line x1="537" y1="701" x2="570" y2="701"/>

      <line x1="666" y1="424" x2="666" y2="457"/>
      <line x1="1064" y1="424" x2="1064" y2="457"/>
      <line x1="666" y1="724" x2="666" y2="756"/>
      <line x1="1064" y1="724" x2="1064" y2="756"/>
      <line x1="610" y1="479" x2="643" y2="479"/>
      <line x1="1087" y1="479" x2="1120" y2="479"/>
      <line x1="610" y1="701" x2="643" y2="701"/>
      <line x1="1087" y1="701" x2="1120" y2="701"/>
    </g>
  </svg>
</main>
</body>
</html>
```